Billboard Design

Billboard design featuring the colors dark teal and dark grey.
Company: Cedarbrook Hollow Properties
Services Real Estate & Management
Phone: 614-739-5081
Important info:
Professionalizing Property Management
Specialized training and credentials in Property Management
Serving single family, multifamily, complexes, and mixed use properties.

UPDATE: We have uploaded photos from a recent project of ours and would love to see them used on the billboard.

```html
<!DOCTYPE html>
<html lang="en">
<head>
<meta charset="UTF-8">
<title>Cedarbrook Hollow Properties — Billboard</title>
<link rel="stylesheet" href="https://fonts.googleapis.com/css2?family=Roboto:wght@400;500;700&display=swap">
<style>
  :root {
    --page-bg: #f1f2f4;
    --board-white: #ffffff;
    --teal-dark: #1c3640;
    --accent-red: #d9141b;
    --text-light: #ffffff;
    --rule-grey: #5a6a70;
    --photo-sky: #9fb9cc;
    --photo-house: #b0675a;
    --photo-lawn: #6f8a55;
  }
  html, body {
    margin: 0;
    padding: 0;
    width: 1200px;
    height: 1200px;
    overflow: hidden;
    background: var(--page-bg);
  }
  .canvas {
    position: relative;
    width: 1200px;
    height: 1200px;
  }
  .billboard {
    position: absolute;
    left: 30px;
    top: 372px;
    width: 1140px;
    height: 456px;
    display: block;
    box-shadow: 0 6px 18px rgba(0,0,0,0.12);
  }
  .billboard text {
    font-family: "Roboto", Arial, sans-serif;
  }
  .brand-title { fill: var(--text-light); font-weight: 700; font-size: 24px; }
  .brand-tagline { fill: var(--text-light); font-weight: 400; font-size: 12.5px; }
  .services-heading { fill: var(--text-light); font-weight: 700; font-size: 24px; }
  .services-copy { fill: var(--text-light); font-weight: 400; font-size: 11px; }
  .services-copy .highlight { fill: var(--accent-red); }
  .logo-name { fill: var(--teal-dark); font-weight: 500; font-size: 10.5px; }
  .phone-number { fill: var(--accent-red); font-weight: 400; font-size: 18px; }
</style>
</head>
<body>
<div class="canvas">
  <svg class="billboard" viewBox="0 0 625 250" xmlns="http://www.w3.org/2000/svg" aria-labelledby="board-title">
    <title id="board-title">Cedarbrook Hollow Properties billboard</title>
    <defs>
      <linearGradient id="project-photo-tone" x1="0" y1="0" x2="0" y2="1">
        <stop offset="0" stop-color="var(--photo-sky)"/>
        <stop offset="0.45" stop-color="var(--photo-house)"/>
        <stop offset="0.8" stop-color="var(--photo-lawn)"/>
        <stop offset="1" stop-color="var(--photo-lawn)"/>
      </linearGradient>
    </defs>

    <!-- board surface -->
    <rect class="board-frame" x="0" y="0" width="625" height="250" fill="var(--board-white)"/>

    <!-- teal information panel -->
    <polygon class="info-panel" points="10,7 365,7 315,187 10,187" fill="var(--teal-dark)"/>

    <!-- diagonal accent stripe -->
    <polygon class="accent-stripe" points="382,7 397,7 290,240 275,240" fill="var(--teal-dark)"/>

    <!-- project photo area -->
    <polygon class="project-photo" role="img"
             aria-label="Photo from a recent project: a red brick Victorian house with a turret and lawn, with two smiling young agents in front"
             points="403,7 618,7 618,240 296,240" fill="url(#project-photo-tone)"/>

    <!-- headline -->
    <text class="brand-title" x="180" y="48" text-anchor="middle">Cedarbrook Hollow Properties</text>
    <text class="brand-tagline" x="180" y="67" text-anchor="middle">Services Real Estate &amp; Management</text>

    <!-- services -->
    <text class="services-heading" x="155" y="112" text-anchor="middle">Our Services</text>
    <text class="services-copy" text-anchor="middle">
      <tspan x="153" y="138">Professionalizing <tspan class="highlight">Property Management</tspan></tspan>
      <tspan x="153" y="152">Specialized <tspan class="highlight">training and credentials</tspan> in Property</tspan>
      <tspan x="153" y="166"><tspan class="highlight">Management Serving</tspan> single family, <tspan class="highlight">multifamily,</tspan></tspan>
      <tspan x="153" y="180"><tspan class="highlight">complexes,</tspan> and <tspan class="highlight">mixed use properties</tspan></tspan>
    </text>

    <!-- contact strip -->
    <rect class="logo-mark" x="18" y="203" width="14" height="14" fill="var(--teal-dark)"/>
    <text class="logo-name">
      <tspan x="38" y="209">Cedarbrook Hollow</tspan>
      <tspan x="38" y="222">Properties</tspan>
    </text>
    <line class="contact-divider" x1="140" y1="197" x2="140" y2="230" stroke="var(--rule-grey)" stroke-width="1"/>
    <text class="phone-number" x="147" y="220">614-739-5081</text>
  </svg>
</div>
</body>
</html>
```